Brom-leigh Sky Harbour Custom Brokers Limited

Shop online from the USA and Ship to Jamaica
Customs Brokerage, Import Export and logistic Services
Address:- 238-240 Halden Brook Road Kingston Jamaica
Email: info@bromleighskyharbour,com
Web: www.bromleighskyharbour.com
Telephone: (876) 555-0148, (876) 555-0193
flyer should be quarter page must print information on back and front

```html
<!DOCTYPE html>
<html lang="en">
<head>
<meta charset="utf-8">
<title>Brom-leigh Sky Harbour Custom Brokers Limited – Flyer Front</title>
<link href="https://fonts.googleapis.com/css2?family=Fredoka:wght@500;600;700&display=swap" rel="stylesheet">
<style>
  :root {
    --navy: #0e2c55;
    --gold: #f7b81d;
    --white: #ffffff;
    --shadow: #0b1f3d;
  }
  html, body {
    margin: 0;
    padding: 0;
    width: 1200px;
    height: 851px;
    overflow: hidden;
    background: var(--white);
  }
  .flyer {
    position: relative;
    width: 1200px;
    height: 851px;
    overflow: hidden;
    background: var(--white);
    font-family: "Fredoka", "Arial Rounded MT Bold", sans-serif;
  }
  .backdrop {
    position: absolute;
    inset: 0;
    width: 1200px;
    height: 851px;
  }
  .brand {
    position: absolute;
    left: 28px;
    top: 62px;
    width: 320px;
    display: flex;
    align-items: center;
    gap: 12px;
  }
  .brand-dot {
    flex: none;
    width: 46px;
    height: 46px;
    border-radius: 50%;
    background: var(--navy);
  }
  .brand-name {
    margin: 0;
    color: var(--navy);
    font-weight: 600;
    font-size: 20px;
    line-height: 1.15;
    letter-spacing: 0.3px;
    text-transform: uppercase;
  }
  .contact {
    position: absolute;
    left: 28px;
    top: 150px;
    width: 300px;
    margin: 0;
    padding: 0;
    list-style: none;
    color: var(--navy);
    font-weight: 500;
    font-size: 13px;
    line-height: 19px;
  }
  .contact .label { font-weight: 700; }
  .headline {
    position: absolute;
    left: 540px;
    top: 44px;
    width: 520px;
    margin: 0;
    text-align: center;
    font-weight: 700;
    letter-spacing: -2px;
  }
  .headline .line {
    display: block;
    white-space: nowrap;
  }
  .light {
    color: var(--white);
    text-shadow: 3px 3px 0 var(--shadow);
  }
  .dark {
    color: var(--navy);
    text-shadow: 3px 3px 0 var(--white);
  }
  .line-shop { font-size: 60px; line-height: 80px; }
  .line-from { font-size: 60px; line-height: 90px; }
  .line-from .dark { font-size: 80px; }
  .line-ship { font-size: 60px; line-height: 80px; }
  .line-jamaica { font-size: 82px; line-height: 96px; }
  .arrow {
    position: absolute;
    width: 68px;
    height: 34px;
  }
  .arrow-right { left: 1018px; top: 152px; }
  .arrow-left { left: 510px; top: 322px; }
  .services {
    position: absolute;
    left: 40px;
    top: 584px;
    width: 1040px;
    margin: 0;
    text-align: center;
    color: var(--gold);
    font-weight: 700;
    font-size: 64px;
    line-height: 82px;
    letter-spacing: -2px;
    text-shadow: 3px 3px 0 var(--shadow);
  }
</style>
</head>
<body>
<main class="flyer">
  <svg class="backdrop" viewBox="0 0 1200 851">
    <defs>
      <linearGradient id="gold-field" x1="0" y1="0" x2="1" y2="1">
        <stop offset="0" stop-color="#f8bd24"/>
        <stop offset="1" stop-color="#e7a917"/>
      </linearGradient>
      <linearGradient id="navy-field" x1="0" y1="0" x2="1" y2="1">
        <stop offset="0" stop-color="#143563"/>
        <stop offset="0.5" stop-color="#274a75"/>
        <stop offset="1" stop-color="#0e2c55"/>
      </linearGradient>
    </defs>
    <polygon class="gold-panel" role="img" aria-label="Faded world map with dashed flight routes on gold"
             points="529,0 1200,0 1200,549 247,371" fill="url(#gold-field)"/>
    <polygon class="navy-panel" role="img" aria-label="World map with grid lines on navy"
             points="0,354 1200,573 1200,834 0,834" fill="url(#navy-field)"/>
    <rect class="footer-band" x="0" y="834" width="1200" height="17" fill="#f7b81d"/>
  </svg>

  <div class="brand">
    <span class="brand-dot"></span>
    <p class="brand-name">Brom-leigh Sky Harbour<br>Custom Brokers Ltd.</p>
  </div>

  <ul class="contact">
    <li><span class="label">Address:</span> 238-240 Halden Brook Road</li>
    <li>Kingston Jamaica</li>
    <li><span class="label">Email:</span> info@bromleighskyharbour,com</li>
    <li><span class="label">Web:</span> www.bromleighskyharbour.com</li>
    <li><span class="label">Tel:</span> (876) 555-0148, (876) 555-0193</li>
  </ul>

  <h1 class="headline">
    <span class="line line-shop light">Shop online</span>
    <span class="line line-from"><span class="light">from</span> <span class="dark">the USA</span></span>
    <span class="line line-ship light">and Ship</span>
    <span class="line line-jamaica dark">to Jamaica</span>
  </h1>

  <svg class="arrow arrow-right" viewBox="0 0 68 34" aria-hidden="true">
    <polygon points="0,13 42,13 42,0 68,17 42,34 42,21 0,21" fill="#ffffff"/>
  </svg>
  <svg class="arrow arrow-left" viewBox="0 0 68 34" aria-hidden="true">
    <polygon points="68,13 26,13 26,0 0,17 26,34 26,21 68,21" fill="#ffffff"/>
  </svg>

  <h2 class="services">Customs Brokerage, Import Export<br>and logistic Services</h2>
</main>
</body>
</html>
```